Simple but elegant business card/logo design for exclusive beauty business

We need a logo designed for a new elegant and exclusive beauty business called "R". The logo itself should be a stylistic and custom design for the letter "R". We would like the business card to have the logo as the centrepiece on a clean background. Gold Logo on black background or silver on white background.

The business card details should be displayed centre of the card. Details are as follows:

Tamsin Earle
Facebook: /shinesoftlyr
Instagram: /shinesoftlyr

The words "Shine Softly" should also appear somewhere on the card.

Industry/Entity Type

Business

Logo Text

G

Requirements
Must have
• Design must be simple, clean and elegant
Should not have
• The design should not be cluttered

```html
<!DOCTYPE html>
<html lang="en">
<head>
<meta charset="utf-8">
<title>R by Tamsin Earle — Business Card</title>
<link href="https://fonts.googleapis.com/css2?family=Pinyon+Script&family=Monsieur+La+Doulaise&family=Poiret+One&display=swap" rel="stylesheet">
<style>
  :root {
    --stage: #121212;
    --card: #000000;
    --gold: #c9a98a;
    --ink: #ffffff;
  }
  html, body {
    margin: 0;
    width: 1200px;
    height: 1200px;
    overflow: hidden;
    background: var(--stage);
  }
  .card {
    position: absolute;
    background: var(--card);
    color: var(--ink);
    text-align: center;
  }
  .card--front { left: 96px; top: 230px; width: 423px; height: 740px; }
  .card--back  { left: 680px; top: 231px; width: 425px; height: 738px; }

  .brand-name {
    position: absolute;
    left: 0; right: 0;
    font-family: "Poiret One", sans-serif;
    font-weight: 400;
    line-height: 1;
  }
  .card--front .brand-name {
    top: 290px;
    font-size: 150px;
    color: var(--gold);
  }
  .card--back .brand-name {
    top: 30px;
    font-size: 66px;
  }
  .byline {
    position: absolute;
    left: 0; right: 0; top: 101px;
    font-family: "Poiret One", sans-serif;
    font-size: 11px;
  }
  .name {
    position: absolute;
    left: 0; right: 0; top: 238px;
    font-family: "Pinyon Script", cursive;
    font-size: 60px;
    line-height: 1;
  }
  .role {
    position: absolute;
    left: 0; right: 0; top: 300px;
    font-family: "Poiret One", sans-serif;
    font-size: 14px;
  }
  .contact {
    position: absolute;
    left: 0; right: 0;
    font-family: "Poiret One", sans-serif;
    font-size: 15px;
    line-height: 21px;
    margin: 0;
  }
  .contact--phone   { top: 364px; }
  .contact--address { top: 406px; }
  .contact--social  { top: 472px; }
  .tagline {
    position: absolute;
    left: 0; right: 0; top: 602px;
    font-family: "Monsieur La Doulaise", cursive;
    font-size: 46px;
    line-height: 1;
  }
</style>
</head>
<body>
  <section class="card card--front">
    <div class="brand-name">R</div>
  </section>

  <section class="card card--back">
    <div class="brand-name">R</div>
    <div class="byline">by Tamsin Earle</div>
    <div class="name">Tamsin Earle</div>
    <div class="role">Beauty Artist</div>
    <p class="contact contact--phone">+61 400 555 018</p>
    <p class="contact contact--address">14 Willow Crescent<br>Camden Hills</p>
    <p class="contact contact--social">Facebook: /shinesoftlyr<br>Instagram: /shinesoftlyr</p>
    <div class="tagline">Shine Softly.</div>
  </section>
</body>
</html>
```